Business Card for Corinne Waldo

Name: Corinne Waldo
Title: Realtor
Email: Corinne@CorinneWaldoRE.example
Phone: 555-318-7492

On the front of the business card, I would like the photo, the contact information and the Corinne Waldo Logo. The backside is required to have the Broker logo and the required logos. Please use the colors from the logo design. Our company has a classy, professional look.

```html
<!DOCTYPE html>
<html lang="en">
<head>
<meta charset="utf-8">
<title>Corinne Waldo – Business Card</title>
<link rel="stylesheet" href="https://fonts.googleapis.com/css2?family=Cinzel:wght@400;500&family=Montserrat:wght@500;700&display=swap">
<style>
  :root {
    --brand-red: #bb1f36;
    --roof-grey: #4a4a4c;
    --paper: #ffffff;
    --ink: #1b1b1b;
    --backdrop: #2a2a2c;
    --photo-light: #f2f2f2;
    --photo-mid: #9a9a9a;
    --photo-dark: #3a3a3a;
  }
  * { box-sizing: border-box; margin: 0; padding: 0; }
  html, body { width: 1200px; height: 780px; overflow: hidden; }
  body {
    background: var(--backdrop);
    position: relative;
    font-family: "Montserrat", sans-serif;
  }
  .card {
    position: absolute;
    top: 230px;
    width: 560px;
    height: 320px;
    background: var(--paper);
    overflow: hidden;
    box-shadow: 0 12px 30px rgba(0,0,0,.45);
  }
  .card--back { left: 27px; }
  .card--front { left: 613px; }
  .card__shapes { position: absolute; inset: 0; }

  .brand-mark {
    position: absolute;
    display: flex;
    align-items: center;
    gap: 10px;
    font-family: "Cinzel", serif;
    font-weight: 500;
  }
  .brand-mark__square { width: 26px; height: 26px; border: 2px solid currentColor; }
  .brand-mark__name { font-size: 19px; letter-spacing: 1px; line-height: 1; }
  .brand-mark__sub { display: block; font-size: 8px; letter-spacing: 1.5px; text-align: right; margin-top: 3px; }

  .card--back .brand-mark { left: 42px; top: 112px; color: var(--paper); }
  .card--front .brand-mark { left: 318px; top: 30px; color: var(--brand-red); }

  .broker-mark {
    position: absolute;
    left: 60px; top: 222px;
    display: flex; align-items: center; gap: 10px;
    font-family: "Cinzel", serif; color: var(--ink);
  }
  .broker-mark__circle { width: 46px; height: 46px; border-radius: 50%; background: var(--ink); }
  .broker-mark__name { font-size: 15px; letter-spacing: 1px; line-height: 1; }
  .broker-mark__sub { display: block; font-size: 7px; letter-spacing: 1.5px; text-align: center; margin-top: 3px; }

  .compliance-badges {
    position: absolute; right: 30px; top: 238px;
    display: flex; align-items: center; gap: 8px;
  }
  .badge { border: 3px solid var(--ink); }
  .badge--housing { width: 48px; height: 44px; }
  .badge--association { width: 44px; height: 44px; }
  .badge--listing { width: 84px; height: 36px; border-width: 2px; }

  .portrait {
    position: absolute; left: 60px; top: 70px;
    width: 270px; height: 148px;
    background: radial-gradient(ellipse at 45% 45%, var(--photo-mid) 0%, var(--photo-dark) 45%, var(--photo-light) 80%);
  }

  .agent {
    position: absolute; left: 38px; top: 238px; color: var(--paper);
  }
  .agent__name { font-family: "Cinzel", serif; font-size: 25px; letter-spacing: 1px; font-weight: 400; }
  .agent__title { font-size: 13px; font-weight: 700; letter-spacing: .5px; margin-top: 6px; }

  .divider {
    position: absolute; left: 282px; top: 232px;
    width: 1px; height: 64px; background: var(--paper);
  }
  .contact {
    position: absolute; left: 298px; top: 238px;
    list-style: none; color: var(--paper);
    font-size: 12px; font-weight: 500;
  }
  .contact__item { display: flex; align-items: center; gap: 8px; margin-bottom: 12px; }
  .contact__icon { width: 14px; height: 14px; fill: var(--paper); flex: none; }
</style>
</head>
<body>

<section class="card card--back" aria-label="Card back">
  <svg class="card__shapes" viewBox="0 0 560 320" aria-hidden="true">
    <rect width="560" height="320" fill="var(--brand-red)"/>
    <polygon points="0,200 282,200 370,66 560,70 560,84 380,80 300,200" fill="var(--roof-grey)"/>
    <polygon points="0,200 300,200 380,80 560,84 560,320 0,320" fill="var(--paper)"/>
    <g fill="var(--roof-grey)">
      <rect x="410" y="100" width="10" height="10"/><rect x="422" y="100" width="10" height="10"/>
      <rect x="410" y="112" width="10" height="10"/><rect x="422" y="112" width="10" height="10"/>
    </g>
  </svg>
  <div class="brand-mark">
    <span class="brand-mark__square"></span>
    <span><span class="brand-mark__name">Corinne Waldo</span><span class="brand-mark__sub">REAL ESTATE</span></span>
  </div>
  <div class="broker-mark">
    <span class="broker-mark__circle"></span>
    <span><span class="broker-mark__name">HARLOW CREST</span><span class="broker-mark__sub">REAL ESTATE</span></span>
  </div>
  <div class="compliance-badges">
    <span class="badge badge--housing"></span>
    <span class="badge badge--association"></span>
    <span class="badge badge--listing"></span>
  </div>
</section>

<section class="card card--front" aria-label="Card front">
  <svg class="card__shapes" viewBox="0 0 560 320" aria-hidden="true">
    <polygon points="318,218 398,84 560,80 560,96 410,100 340,218" fill="var(--roof-grey)"/>
    <polygon points="0,218 340,218 410,100 560,96 560,320 0,320" fill="var(--brand-red)"/>
    <g fill="var(--roof-grey)">
      <rect x="440" y="128" width="10" height="10"/><rect x="452" y="128" width="10" height="10"/>
      <rect x="440" y="140" width="10" height="10"/><rect x="452" y="140" width="10" height="10"/>
    </g>
  </svg>
  <div class="portrait" role="img" aria-label="Black and white portrait photo of Corinne Waldo"></div>
  <div class="brand-mark">
    <span class="brand-mark__square"></span>
    <span><span class="brand-mark__name">Corinne Waldo</span><span class="brand-mark__sub">REAL ESTATE</span></span>
  </div>
  <div class="agent">
    <h1 class="agent__name">CORINNE WALDO</h1>
    <p class="agent__title">REALTOR</p>
  </div>
  <span class="divider"></span>
  <ul class="contact">
    <li class="contact__item">
      <svg class="contact__icon" viewBox="0 0 24 24" aria-hidden="true"><path d="M6.6 10.8a15.1 15.1 0 0 0 6.6 6.6l2.2-2.2a1 1 0 0 1 1-.25 11.4 11.4 0 0 0 3.6.57 1 1 0 0 1 1 1V20a1 1 0 0 1-1 1A17 17 0 0 1 3 4a1 1 0 0 1 1-1h3.5a1 1 0 0 1 1 1c0 1.25.2 2.45.57 3.6a1 1 0 0 1-.25 1z"/></svg>
      <span>555-318-7492</span>
    </li>
    <li class="contact__item">
      <svg class="contact__icon" viewBox="0 0 24 24" aria-hidden="true"><path d="M2 5h20v14H2z M4 7l8 6 8-6" fill="none" stroke="var(--paper)" stroke-width="2"/></svg>
      <span>Corinne@CorinneWaldoRE.example</span>
    </li>
  </ul>
</section>

</body>
</html>
```